Flyer für ambulanten Pflegedienst
Zielgruppe
Ambulanter Pflegedienst in Gründung. Habe schon ein Logo und Text. Zielgruppe sind Pflege und Hilfsbedürftige Menschen

```html
<!DOCTYPE html>
<html lang="de">
<head>
<meta charset="utf-8">
<title>Pflege Hafen – Flyer</title>
<link rel="stylesheet" href="https://fonts.googleapis.com/css2?family=Rasa:wght@500;600;700&family=Open+Sans:wght@400;600;700&display=swap">
<style>
  :root {
    --teal: #4fb5ab;
    --teal-dark: #3a9c96;
    --blue: #3d92ad;
    --band-a: #3b8fb3;
    --band-b: #55bcb2;
    --text: #333;
    --paper: #fff;
    --bg: #ececec;
    --photo-a: #c9dbe0;
    --photo-b: #e8d8c8;
    --leaf: #bfe3de;
  }
  * { margin: 0; padding: 0; box-sizing: border-box; }
  html, body { width: 1200px; height: 623px; overflow: hidden; background: var(--bg); }
  body { position: relative; font-family: "Open Sans", sans-serif; color: var(--text); }
  .page { position: absolute; background: var(--paper); overflow: hidden; box-shadow: 0 4px 12px rgba(0,0,0,.12); }
  .serif { font-family: "Rasa", serif; }
  .abs { position: absolute; }
  .band { position: absolute; left: 0; right: 0; bottom: 0; height: 28px; background: linear-gradient(90deg, var(--band-a), var(--band-b)); color: #fff; font-weight: 600; font-size: 11px; display: flex; align-items: center; padding: 0 14px; }

  /* Cover */
  .cover { left: 73px; top: 54px; width: 340px; height: 530px; }
  .brand-mark { left: 22px; top: 30px; width: 60px; height: 60px; border-radius: 50%; background: var(--teal); }
  .brand-name { left: 118px; top: 28px; font-family: "Rasa", serif; font-weight: 700; font-size: 40px; color: var(--blue); line-height: 1; }
  .brand-sub { left: 119px; top: 88px; font-family: "Rasa", serif; font-size: 11px; color: var(--teal-dark); line-height: 1.5; }
  .brand-sub .small { display: block; text-align: center; letter-spacing: 1.5px; font-size: 10px; }
  .services { top: 143px; font-family: "Rasa", serif; font-size: 11.5px; color: var(--teal-dark); line-height: 1.15; }
  .services li { list-style: none; margin-bottom: 6px; }
  .services small { font-size: 8px; display: block; }
  .cover-photo { left: 60px; top: 250px; width: 420px; height: 420px; border-radius: 50%; background: linear-gradient(135deg, var(--photo-a), #a9c4cd 60%, var(--photo-b)); }
  .leaves { border-radius: 50%; background: var(--leaf); opacity: .7; }
  .tag-circle { left: 8px; top: 310px; width: 150px; height: 150px; border-radius: 50%; background: var(--teal); color: #fff; font-family: "Rasa", serif; font-size: 11.5px; line-height: 1.35; display: flex; align-items: center; justify-content: center; text-align: center; padding: 10px; }
  .cover .band { justify-content: flex-end; }

  /* Spread */
  .spread-left { left: 467px; top: 54px; width: 342px; height: 530px; box-shadow: none; }
  .spread-right { left: 809px; top: 54px; width: 342px; height: 530px; box-shadow: none; }
  .spread-shadow { position: absolute; left: 467px; top: 54px; width: 684px; height: 530px; box-shadow: 0 4px 12px rgba(0,0,0,.12); }
  .spread-band { position: absolute; left: 467px; top: 556px; width: 684px; height: 28px; background: linear-gradient(90deg, var(--band-a), var(--band-b)); color: #fff; font-weight: 600; font-size: 11px; display: flex; align-items: center; justify-content: space-between; padding: 0 14px 0 22px; letter-spacing: .3px; }
  .h2 { font-family: "Rasa", serif; font-weight: 600; color: var(--blue); font-size: 13px; line-height: 1.1; }
  .h2 small { display: block; font-size: 8.5px; font-weight: 500; }
  .lead { font-size: 7.6px; font-weight: 600; color: var(--blue); line-height: 1.65; }
  .list { font-size: 7.8px; line-height: 1.6; list-style: none; }
  .body { font-size: 7.6px; line-height: 1.62; }
  .just { text-align: justify; }
  .inner-photo { left: 150px; top: -16px; width: 216px; height: 216px; border-radius: 50%; background: linear-gradient(150deg, #d9c6b4, var(--photo-a) 65%); }
  .goal-circle { left: 115px; top: 128px; width: 100px; height: 100px; border-radius: 50%; background: var(--teal); color: #fff; font-size: 7.8px; font-weight: 600; line-height: 1.55; display: flex; align-items: center; justify-content: center; text-align: center; padding: 8px; }
  .right-photo { left: 143px; top: 340px; width: 254px; height: 254px; border-radius: 50%; background: linear-gradient(160deg, var(--photo-b), #cfd9d6 60%); }
</style>
</head>
<body>

<!-- Cover -->
<section class="page cover">
  <div class="abs brand-mark"></div>
  <div class="abs brand-name">Pflege Hafen</div>
  <div class="abs brand-sub">ambulanter Pflegedienst Albrecht UG<span class="small">— Haftungsbeschränkt —</span></div>

  <ul class="abs services" style="left:64px">
    <li>Grundpflege</li>
    <li>Behandlungspflege</li>
    <li>24-Stunden Pflege</li>
    <li>Hauswirtschaftlicher<br>Versorgung</li>
  </ul>
  <ul class="abs services" style="left:198px">
    <li>Betreuungs- und<br>Entlastungsleistungen<small>nach § 45 SGB XI</small></li>
    <li>Verhinderungspflege</li>
    <li>Alltagsbegleitung</li>
  </ul>

  <div class="abs cover-photo" role="img" aria-label="Foto: offene Hände halten ein Papierherz mit einem älteren Paar"></div>
  <div class="abs leaves" style="left:8px;top:250px;width:120px;height:70px" role="img" aria-label="Dekorative Blätter"></div>
  <div class="abs tag-circle">Wir stehen<br>für hochwertige<br>&amp; individuelle<br>Unterstützungen<br>mit Herz - für ein<br>selbstbestimmtest<br>Leben zu<br>Hause</div>
  <div class="band">www.pflege-hafen.de</div>
</section>

<!-- Inner spread -->
<div class="spread-shadow"></div>
<section class="page spread-left">
  <div class="abs inner-photo" role="img" aria-label="Foto: Pflegerin kämmt einer älteren Dame die Haare"></div>
  <div class="abs leaves" style="left:62px;top:180px;width:70px;height:70px" role="img" aria-label="Dekorative Blätter"></div>
  <div class="abs leaves" style="left:280px;top:205px;width:45px;height:45px" role="img" aria-label="Dekorative Blätter"></div>

  <h2 class="abs h2" style="left:22px;top:26px">Verhinderungs-<br>pflege</h2>
  <p class="abs lead" style="left:22px;top:65px;width:125px">Das Angebot im Bereich der Verhinderungspflege richtet sich an die Angehörigen, die bei der Pflege stundenweise Entlastung benötigen. Typische Anlässe sind z.B.</p>
  <ul class="abs list" style="left:22px;top:154px">
    <li>Krankheit</li><li>Überlastung</li><li>Urlaub</li>
  </ul>
  <div class="abs goal-circle">Das oberste Ziel der Pflege ist die Sicherung und Verbesserung der Lebensqualität.</div>

  <h2 class="abs h2" style="left:22px;top:252px">Betreuungs- und<br>Entlastungsleistungen<small>nach § 45 SGB XI</small></h2>
  <p class="abs lead" style="left:22px;top:305px;width:150px">Voraussetzung ist das Vorliegen eines Pflegegrades. Bei der Antragsstellung eines Pflegegrades sind wir behilflich und begleiten die Begutachtung durch den Medizinischen Dienst der Krankenkasse.</p>
  <ul class="abs list" style="left:22px;top:389px;width:150px">
    <li>Unterstützung bei der Haushaltsführung</li>
    <li>Einkaufen</li>
    <li>Begleitung zu Ärzten</li>
    <li>Arzttermine vereinbaren</li>
    <li>Unterstützung beim Ausfüllen von Formularen und Anträgen</li>
    <li>Spaziergänge</li>
  </ul>

  <h2 class="abs h2" style="left:195px;top:252px">Alltagsbegleitung</h2>
  <p class="abs lead" style="left:195px;top:277px;width:140px">In er Alltagsbegleitung werden die Pflegepersonen in allen alltäglichen Tätigkeiten und Freizeitaktivitäten unterstützen und begleiten. Typische Leistungen sind z.B.</p>
  <ul class="abs list" style="left:195px;top:354px">
    <li>Arztbesuche</li><li>Behördengänge</li><li>Kulturelle Veranstaltungen</li><li>Spaziergänge</li><li>Ausflüge</li><li>Wanderungen</li><li>Stadtbummel</li><li>Restaurantbesuche</li><li>Friseurbesuche</li><li>Gedächtnistraining usw.</li>
  </ul>
</section>

<section class="page spread-right">
  <div class="abs right-photo" role="img" aria-label="Foto: junge Frau und ältere Dame schauen gemeinsam auf ein Tablet"></div>

  <h2 class="abs h2" style="left:29px;top:24px">Gerne helfen wir Ihnen weiter</h2>
  <p class="abs body" style="left:29px;top:49px;width:290px">Der Altenpflege- und Seniorenbetreuungsdienst führt sämtliche Pflegeleistungen kompetent, professionell und zuverlässig aus. Das oberste Ziel der Pflege ist die Sicherung und Verbesserung der Lebensqualität und das Bewahren des gewohnten Lebensumfelds der Pflegepersonen.<br>Krankenhaus- und Bereuungsheimaufenthalte sollen möglichst vermieden werden. Diesen Grundgedanken liegt die Erkenntnis zu Grunde, dass <b>in einer vertrauten Umgebung Kranke oft schneller gesünder werden</b> und gerade ältere Menschen sich zu Hause besonders wohl und geborgen fühlen.</p>
  <p class="abs body" style="left:29px;top:156px;width:290px;font-weight:700">Der grundlegende Geschäftsprozess des Unternehmens gliedert sich in die Bereiche Beratung, Pflegekonzept, Vertragsabschluss und Pflege:</p>

  <h2 class="abs h2" style="left:29px;top:196px">Beratung</h2>
  <p class="abs body just" style="left:29px;top:220px;width:138px">Kunden werden ausführlich unter Berücksichtigung ihrer Wünsche und Vorstellungen beraten. Denn das vorhandene Pflegeangebot bietet eine Vielzahl an Möglichkeiten. Wichtig ist der Aufbau von Vertrauen.</p>

  <h2 class="abs h2" style="left:29px;top:309px">Pflegekonzept</h2>
  <p class="abs body" style="left:29px;top:335px;width:138px">Unter Berücksichtigung aller Möglichkeiten und Patientenwünsche wird ein individuelles Leistungsangebot entwickelt und eine verbindliche Kostenaufstellung erstellt.</p>

  <h2 class="abs h2" style="left:29px;top:410px">Vertragsabschluss</h2>
  <p class="abs body" style="left:29px;top:436px;width:112px">Alle Aufträge mit Kunden werden in schriftlicher Form geschlossen und beidseitig unterzeichnet.</p>

  <h2 class="abs h2" style="left:189px;top:198px">Pflege</h2>
  <p class="abs body just" style="left:189px;top:221px;width:136px">Die vereinbarten Pflegeleistungen werden nun umgesetzt. Dabei kann der Kunde stets eine hohe Ausführungsqualität erwarten. Es wird für jeden Kunden eine Mappe zur Pflegedokumentation geführt (Pflegesoftware, die stets vom Kunden sowie seinen Angehörigen eingesehen werden kann).</p>
</section>

<div class="spread-band"><span>Sie erreichen uns unter 0123 – 98 76 54</span><span>www.pflege-hafen.de</span></div>

</body>
</html>
```